Mobile (Android/iPhone) game studio needs stationary design and a business card

We are Brisk Pebble Software and we need a fun and creative stationary design. Our company builds Android and iPhone games and children's software. The stationary designs should reflect an entertainment, fun and creativity. The pieces of stationary we need are:
1. A4 and Letter Word template (company letterhead)
2. A4 and Letter PPT template
3. Business card
4. Envelopes of various standard sizes
Each of the designs should somehow utilize our company logo.
The business card should have the following:
1. Incorporates our company logo (see attached)
2. Has a front and back with the same design (front is English, back is Traditional Chinese)
3. Delivered in an editable template so we can easily add new business cards using the same template when we hire more employees
4. Field for full name
5. Field for employee's title
6. Field for employee's email address
7. Field for company phone number - +886-2-25118340
8. Field for mobile phone number
9. Field for company fax number - +886-2-25118472
10. Company website address: www.briskpebble-example.com
11. Company address (on English side): 2F-7, NO. 26, Lane 91, Fulin Road, Nei Hu District, Taipei Taiwan
12. Company address (on Traditional Chinese side): See Word document attachment for address in Chinese characters

```html
<!DOCTYPE html>
<html lang="en">
<head>
<meta charset="utf-8">
<title>Brisk Pebble Software — Letterhead Set</title>
<link rel="stylesheet" href="https://fonts.googleapis.com/css2?family=Open+Sans:wght@400;600;700&display=swap">
<style>
  :root {
    --backdrop: #e4e4e4;
    --paper: #ffffff;
    --brand-blue: #1a8fd6;
    --brand-deep: #0058a8;
    --brand-mid: #0a8ed6;
    --brand-light: #7cc8ef;
    --ink-grey: #9a9ea3;
    --rule-blue: #2a9ae0;
  }
  * { box-sizing: border-box; margin: 0; padding: 0; }
  html, body {
    width: 1200px;
    height: 854px;
    overflow: hidden;
    background: var(--backdrop);
    font-family: "Open Sans", Arial, sans-serif;
  }
  .sheet {
    position: absolute;
    background: var(--paper);
    overflow: hidden;
  }
  .sheet-first { left: 180px; top: 138px; width: 458px; height: 648px; z-index: 2; }
  .sheet-continuation { left: 556px; top: 73px; width: 457px; height: 649px; z-index: 1; overflow: visible; }

  .brand { position: absolute; display: flex; align-items: center; }
  .brand-dot { border-radius: 50%; background: var(--brand-blue); flex: none; }
  .brand-name { font-weight: 700; color: var(--brand-blue); line-height: 1; white-space: nowrap; }

  .sheet-first .brand { left: 33px; top: 37px; gap: 11px; }
  .sheet-first .brand-dot { width: 36px; height: 36px; }
  .sheet-first .brand-name { font-size: 14px; }

  .sheet-continuation .brand { left: 32px; top: 35px; gap: 6px; }
  .sheet-continuation .brand-dot { width: 22px; height: 22px; }
  .sheet-continuation .brand-name { font-size: 8.5px; }

  .contact {
    position: absolute;
    left: 81px;
    top: 89px;
    font-style: normal;
    font-size: 6.6px;
    line-height: 8.2px;
    color: var(--ink-grey);
    white-space: nowrap;
  }
  .contact-rule { width: 38px; height: 1.5px; background: var(--rule-blue); margin-bottom: 5px; }
  .contact .label { color: var(--rule-blue); margin-right: 3px; }

  .web-band {
    position: absolute;
    left: 25px;
    width: 408px;
    height: 27px;
    border-radius: 14px;
    background: linear-gradient(90deg, var(--brand-deep) 0%, var(--brand-mid) 70%, var(--brand-light) 82%, var(--brand-light) 100%);
  }
  .sheet-first .web-band { top: 595px; }
  .sheet-continuation .web-band { top: 596px; height: 26px; }
  .web-address {
    position: absolute;
    right: 92px;
    top: 0;
    line-height: 27px;
    font-size: 10px;
    font-weight: 600;
    color: #ffffff;
    white-space: nowrap;
  }
  .band-badge { position: absolute; left: 324px; top: -14px; }
</style>
</head>
<body>
  <section class="sheet sheet-continuation">
    <header class="brand">
      <span class="brand-dot" aria-hidden="true"></span>
      <span class="brand-name">Brisk Pebble Software</span>
    </header>
    <footer class="web-band">
      <span class="web-address">www.briskpebble-example.com</span>
      <svg class="band-badge" width="54" height="54" viewBox="0 0 54 54" aria-hidden="true">
        <defs>
          <radialGradient id="badgeFillBack" cx="40%" cy="35%" r="70%">
            <stop offset="0%" stop-color="#3aaef0"/>
            <stop offset="100%" stop-color="#0062b4"/>
          </radialGradient>
        </defs>
        <circle cx="27" cy="27" r="27" fill="url(#badgeFillBack)"/>
      </svg>
    </footer>
  </section>

  <main class="sheet sheet-first">
    <header class="brand">
      <span class="brand-dot" aria-hidden="true"></span>
      <span class="brand-name">Brisk Pebble Software</span>
    </header>

    <address class="contact">
      <div class="contact-rule"></div>
      <div>2F-7, NO. 26, Lane 91, Fulin Road</div>
      <div>Nei Hu District, Taipei Taiwan</div>
      <div><span class="label">P</span>+886-2-25118340</div>
      <div><span class="label">F</span>+886-2-25118472</div>
    </address>

    <footer class="web-band">
      <span class="web-address">www.briskpebble-example.com</span>
      <svg class="band-badge" width="54" height="54" viewBox="0 0 54 54" aria-hidden="true">
        <defs>
          <radialGradient id="badgeFillFront" cx="40%" cy="35%" r="70%">
            <stop offset="0%" stop-color="#3aaef0"/>
            <stop offset="100%" stop-color="#0062b4"/>
          </radialGradient>
        </defs>
        <circle cx="27" cy="27" r="27" fill="url(#badgeFillFront)"/>
      </svg>
    </footer>
  </main>
</body>
</html>
```